Swimming Pool Supply Company Business Cards

We need business cards designed for company. These need to be easy to edit so that we can fill in names, titles, and contact info for each person who works here.

Dalton R. Pembry
Manager of Legal & Finance
J.L. Pembry, Incorporated

4837 Grelwood Avenue
Marlow Crossing, PA 19054

E. dalton@jlpembry.com
M. (215) 555-7193
O. (215) 555-4620

Contact Information for Business Card

Looking to upgrade current business cards with graphic that can be edited. Looking for fresh ideas for an age old industry.

Font styles to use
Serif
Sans Serif

Colors

Designer to choose colors to be used in the design.

Requirements
Must have
• Professional, fresh, unique but professional

```html
<!DOCTYPE html>
<html lang="en">
<head>
<meta charset="utf-8">
<title>Pembry Business Cards</title>
<link rel="stylesheet" href="https://fonts.googleapis.com/css2?family=Lato:wght@400;700;900&display=swap">
<style>
  :root {
    --stage: #161616;
    --card: #222222;
    --blue: #1565b8;
    --line-blue: #1a5fa8;
    --white: #ffffff;
    --text: #f2f2f2;
  }
  * { margin: 0; padding: 0; box-sizing: border-box; }
  html, body {
    width: 1200px; height: 912px; overflow: hidden;
    background: var(--stage);
    font-family: "Lato", Arial, sans-serif;
    color: var(--text);
  }
  .stage {
    position: relative; width: 1200px; height: 912px;
  }
  .card {
    position: absolute; left: 250px; width: 700px; height: 400px;
    background: var(--card);
    overflow: hidden;
    box-shadow: 0 10px 30px rgba(0,0,0,.6);
  }
  .card--front { top: 40px; }
  .card--back { top: 472px; }

  .brand-name {
    font-weight: 900; color: var(--blue);
    letter-spacing: 2px; line-height: 1;
  }
  .tagline { font-size: 17px; color: var(--text); margin-top: 10px; }

  .card--front .brand {
    position: absolute; left: 0; right: 0; top: 130px; text-align: center;
  }
  .card--front .brand-name { font-size: 104px; }
  .card--front .tagline { font-size: 20px; margin-top: 14px; }

  .card--back .brand { position: absolute; left: 40px; top: 62px; }
  .card--back .brand-name { font-size: 78px; }

  .divider {
    position: absolute; left: 40px; right: 40px; top: 212px;
    height: 1px; background: var(--line-blue);
  }
  .person {
    position: absolute; right: 40px; top: 56px; text-align: right;
  }
  .person-name { font-size: 27px; color: var(--blue); font-weight: 400; }
  .person-title { font-size: 17px; margin-top: 2px; }
  .address {
    position: absolute; right: 40px; top: 112px; text-align: right;
    font-size: 16px; line-height: 1.35;
  }
  .contacts {
    position: absolute; left: 40px; top: 244px;
    list-style: none; font-size: 19px; line-height: 1.35;
  }
  .contacts li { display: flex; align-items: center; gap: 12px; }
  .contacts svg { width: 16px; height: 16px; fill: var(--blue); flex: none; }
  .swoosh { position: absolute; left: 0; top: 0; }
  .website {
    position: absolute; right: 28px; bottom: 18px;
    font-size: 16px; color: var(--white);
  }
</style>
</head>
<body>
<main class="stage">
  <section class="card card--front">
    <div class="brand">
      <div class="brand-name">PEMBRY</div>
      <p class="tagline">Big Enough to Serve You, Small Enough to Care</p>
    </div>
  </section>

  <section class="card card--back">
    <div class="brand">
      <div class="brand-name">PEMBRY</div>
      <p class="tagline">Swimming Pools, Supplies, and Accessories</p>
    </div>

    <div class="person">
      <h1 class="person-name">Dalton R. Pembry</h1>
      <p class="person-title">Manager of Legal &amp; Finance</p>
    </div>
    <address class="address" style="font-style:normal">
      J.L. Pembry, Incorporated<br>
      4837 Grelwood Avenue<br>
      Marlow Crossing, PA 19054
    </address>

    <div class="divider"></div>

    <ul class="contacts">
      <li>
        <svg viewBox="0 0 16 16"><path d="M3 1l3 3-1.5 2c1 2 3 4 5 5L11.5 9.5l3 3L12.5 15C6 14 2 10 1 3.5z"/></svg>
        (215) 555-4620
      </li>
      <li>
        <svg viewBox="0 0 16 16"><path d="M4 0h8v16H4zM5.5 2v9h5V2zM7 12.5h2v2H7z"/></svg>
        (215) 555-7193
      </li>
      <li>
        <svg viewBox="0 0 16 16"><path d="M0 3h16v10H0zM1.5 4.5l6.5 5 6.5-5z" fill-rule="evenodd"/></svg>
        dalton@jlpembry.com
      </li>
    </ul>

    <svg class="swoosh" width="700" height="400" viewBox="0 0 700 400">
      <path d="M330 400 C430 360 560 300 700 250 L700 400 Z" fill="var(--blue)"/>
      <path d="M250 400 C360 340 480 300 600 272 C480 305 380 350 330 400 Z" fill="var(--white)"/>
    </svg>
    <p class="website">www.jlpembry.com</p>
  </section>
</main>
</body>
</html>
```